Brochure Projecct

I need a brochure created for my company, which will be sent to customers via email in PDF format. I have uploaded the company logo with this project, which I want incorporated in the design.

Designers should view the company website at www.brightcounselpages.com. I want the brochure to compliment the website (i.e., very clean design). I would also like pictures added to the brochure to make the design visually stunning.

In terms of content, I need four pages in the brochure to add four separate sections of content (one section per page). The four sections of content will be as follows (1) Search Engine Optimization Benefits (2) Increased Client Retention (3) Showcase Your Law Firm (4) Maximize Your Online ROI (5) Pricing Plans. I will give the content to the winning designer to add to the project. Each individual content section will have four subsection titles after which content of approximately 100 to 200 words will appear.

Designers can decide if other pages should be added to the brochure (i.e., a "cover page" that would have little content, but be visually appealing like the cover of a book - - - a "back page" that may just have the logo, contact information, etc).

My company address and email address should be prominently featured through every page (address: 2715 West Juniper Avenue, Suite 1400, Scottsdale, Arizona 85317; email: sales@brightcounselpages.com).

Industry/Entity Type

It Company

Requirements
Must have
• Clean look but visually stunning incorporating the design of the website at brightcounselpages.com as well as the logo. Also, room for content as set forth in the description of this project.

```html
<!DOCTYPE html>
<html lang="en">
<head>
<meta charset="utf-8">
<title>Bright Counsel Pages – Brochure</title>
<link href="https://fonts.googleapis.com/css2?family=Arimo:wght@400;700&family=Mulish:ital,wght@0,400;0,600;1,800&display=swap" rel="stylesheet">
<style>
  :root {
    --backdrop: #4a3a31;
    --page: #f4f5f7;
    --page-shade: #e3e5e9;
    --ink: #1c1c1c;
    --ink-soft: #333;
    --blue: #1f6fb0;
    --blue-deep: #1c4f86;
    --cyan: #35b7e0;
    --cyan-light: #7fd6f2;
    --tab: #141414;
    --white: #ffffff;
  }
  * { box-sizing: border-box; margin: 0; padding: 0; }
  html, body { width: 1200px; height: 763px; overflow: hidden; }
  body { background: var(--backdrop); position: relative; font-family: "Mulish", sans-serif; }

  .page {
    position: absolute; top: 34px; width: 537px; height: 694px;
    background: linear-gradient(180deg, var(--page-shade) 0%, var(--page) 35%, var(--white) 70%, var(--page) 100%);
    overflow: hidden;
  }
  .page--cover { left: 42px; }
  .page--inner { left: 622px; }

  /* brand */
  .brand { position: absolute; display: flex; align-items: center; gap: 8px;
    font-family: "Arimo", sans-serif; font-weight: 700; color: var(--ink); }
  .brand__dot { border-radius: 50%; background: var(--blue); flex: none; }
  .page--cover .brand { left: 0; right: 0; top: 100px; justify-content: center; font-size: 30px; }
  .page--cover .brand__dot { width: 26px; height: 26px; }
  .page--inner .brand { right: 14px; top: 30px; width: 90px; font-size: 11px; line-height: 13px;
    flex-direction: column; gap: 5px; text-align: center; }
  .page--inner .brand__dot { width: 26px; height: 26px; }

  /* rails */
  .rail { position: absolute; height: 5px;
    background: linear-gradient(90deg, var(--blue) 0%, var(--cyan-light) 50%, var(--blue) 100%); }
  .rail::before, .rail::after { content: ""; position: absolute; top: -4px; width: 11px; height: 11px;
    border: 2px solid var(--cyan); border-radius: 50%; background: var(--white); }
  .rail::before { left: -14px; }
  .rail::after { right: -14px; }

  .photo { position: absolute; }
  .photo--books { left: 60px; top: 208px; width: 420px; height: 280px;
    background: linear-gradient(180deg, #2a1710 0%, #6b3a22 22%, #9a5a34 45%, #3a2014 58%, #d9c7ae 72%, #f1e6d6 82%, #5a4032 100%); }
  .photo--gavel { left: 155px; top: 107px; width: 347px; height: 225px;
    background: linear-gradient(135deg, #4a1a12 0%, #8b2e1c 30%, #a05a2c 55%, #7a3a18 75%, #c0703c 100%); }

  .mission { position: absolute; left: 47px; top: 527px; width: 444px; height: 93px;
    border: 1px solid var(--blue); border-radius: 10px; padding: 5px 12px; }
  .mission__inner { background: var(--white); border-radius: 10px; height: 100%;
    box-shadow: 0 0 6px rgba(0,0,0,.18);
    font-family: "Arimo", sans-serif; font-size: 10.6px; line-height: 17.5px; color: var(--ink);
    text-align: center; padding-top: 14px; }

  .footer { position: absolute; left: 0; right: 0; top: 646px; height: 25px;
    background: linear-gradient(180deg, var(--blue) 0%, var(--blue-deep) 100%);
    color: var(--white); font-size: 7.6px; display: flex; align-items: center; padding-left: 31px; gap: 5px; }
  .footer__sep { opacity: .8; }
  .footer-lines { position: absolute; left: 0; right: 0; top: 673px; height: 21px;
    border-top: 2px solid #9aa3ad; background: linear-gradient(180deg, #cfd3d8, #eef0f2); }

  .section-title { position: absolute; left: 58px; top: 50px; font-weight: 800; font-style: italic;
    font-size: 14px; line-height: 18px; color: var(--ink); }
  .bubble { position: absolute; left: 38px; top: 163px; }
  .bubble__text { position: absolute; left: 38px; top: 203px; width: 150px; text-align: center;
    color: var(--white); font-weight: 800; font-style: italic; font-size: 13.5px; line-height: 17px; }

  .topics { position: absolute; left: 32px; top: 345px; width: 474px; }
  .topic { height: 75px; }
  .topic__tab { display: inline-block; background: var(--tab); color: var(--cyan);
    font-family: "Arimo", sans-serif; font-weight: 700; font-size: 11.5px;
    padding: 2px 8px; border-radius: 3px 3px 3px 0; height: 19px; line-height: 15px; }
  .topic__body { font-size: 6.4px; line-height: 9.4px; color: var(--ink-soft); margin-top: 4px; text-align: justify; }
</style>
</head>
<body>

<section class="page page--cover">
  <div class="brand"><span class="brand__dot"></span>Bright Counsel Pages</div>

  <div class="rail" style="left:60px; top:202px; width:420px;"></div>
  <div class="photo photo--books" role="img" aria-label="Photo of an open law book in front of a row of leather-bound volumes"></div>
  <div class="rail" style="left:60px; top:489px; width:420px;"></div>

  <div class="mission">
    <div class="mission__inner">
      Bright Counsel Pages exists to connect people searching for the best lawyer for<br>
      their case with local attorneys and law firms having an established reputation in<br>
      their legal practice areas of being the best of the best in their areas of law.
    </div>
  </div>

  <footer class="footer">
    <span>2715 West Juniper Avenue, Suite 1400, Scottsdale, Arizona 85317</span><span class="footer__sep">|</span>
    <span>sales@brightcounselpages.com</span><span class="footer__sep">|</span>
    <span>www.brightcounselpages.com</span>
  </footer>
  <div class="footer-lines"></div>
</section>

<section class="page page--inner">
  <h1 class="section-title">Search Engine Optimization Benefits</h1>
  <div class="rail" style="left:50px; top:75px; width:360px;"></div>
  <div class="brand"><span class="brand__dot"></span>Bright Counsel Pages</div>

  <div class="photo photo--gavel" role="img" aria-label="Photo of a wooden judge's gavel in front of law books"></div>

  <svg class="bubble" width="170" height="130" viewBox="0 0 170 130" aria-hidden="true">
    <defs>
      <linearGradient id="bubbleFill" x1="0" y1="0" x2="0" y2="1">
        <stop offset="0" stop-color="#1f8fc4"/>
        <stop offset="1" stop-color="#4cc6ea"/>
      </linearGradient>
    </defs>
    <ellipse cx="75" cy="60" rx="74" ry="58" fill="url(#bubbleFill)"/>
    <path d="M118 100 L138 126 L128 92 Z" fill="#4cc6ea"/>
  </svg>
  <p class="bubble__text">A Local<br>List of Experienced<br>Arizona Lawyers</p>

  <div class="topics">
    <article class="topic">
      <h2 class="topic__tab">SubTitle1</h2>
      <p class="topic__body">Our search pages place your practice in front of people who are already looking for legal help in their own city. Each profile is written to match the words clients type, so your firm appears higher in results and earns more visits. We track rankings monthly and adjust titles, reviews and practice areas to keep steady growth. Clear reports show where new calls and emails come from each month.</p>
    </article>
    <article class="topic">
      <h2 class="topic__tab">SubTitle2</h2>
      <p class="topic__body">Our search pages place your practice in front of people who are already looking for legal help in their own city. Each profile is written to match the words clients type, so your firm appears higher in results and earns more visits. We track rankings monthly and adjust titles, reviews and practice areas to keep steady growth. Clear reports show where new calls and emails come from each month.</p>
    </article>
    <article class="topic">
      <h2 class="topic__tab">SubTitle3</h2>
      <p class="topic__body">Our search pages place your practice in front of people who are already looking for legal help in their own city. Each profile is written to match the words clients type, so your firm appears higher in results and earns more visits. We track rankings monthly and adjust titles, reviews and practice areas to keep steady growth. Clear reports show where new calls and emails come from each month.</p>
    </article>
    <article class="topic">
      <h2 class="topic__tab">SubTitle4</h2>
      <p class="topic__body">Our search pages place your practice in front of people who are already looking for legal help in their own city. Each profile is written to match the words clients type, so your firm appears higher in results and earns more visits. We track rankings monthly and adjust titles, reviews and practice areas to keep steady growth. Clear reports show where new calls and emails come from each month.</p>
    </article>
  </div>

  <footer class="footer">
    <span>2715 West Juniper Avenue, Suite 1400, Scottsdale, Arizona 85317</span><span class="footer__sep">|</span>
    <span>sales@brightcounselpages.com</span><span class="footer__sep">|</span>
    <span>www.brightcounselpages.com</span>
  </footer>
  <div class="footer-lines"></div>
</section>

</body>
</html>
```